Dawson's Lawn Service needs a postcard design

I need a design to attract lawn cutting customers. I am a high school junior, focusing on my city and the neighboring city. I think it would be advantageous to let my potential clients know I am earning money for my college education. They should also know, I will be working side by side with my father, who operated his own lawn service for 20 years, so they can be assured of a quality result for their lawn. I will be using state of the art, commercial equipment.

A few things that are unique to my service are; my mower weighs half of what other commercial mowers do (a softer footprint), my mower does NOT throw clippings into mulch or flower beds, at an additional charge I offer bagging of the clippings and/or dog waste clean-up. I am thinking about a two-sided design. I would also like a cartoon style picture of myself riding my mower. If this is something you can create, I can send you a photo of myself and a photo of my mower. If not, I can get this drawing done separately, then send it to you, I would just need to know what kind of file you would need it in. I am not going to have a business name, I want to introduce myself as Dawson to keep it simple and personal. We can add a coupon to the postcard, offering one free cut with commitment to a full 26 week season. The name of my high school is Marwick High.

The cartoon picture attached is our logo.

Target Market(s)

Homeowners that use a commercial lawn cutting service, homeowners that need a temporary service while they are on vacation

Industry/Entity Type

School

Colors
3176b5
9bcb3c

Requirements
Must have
• An appeal for people to want to help me earn money for my college education. A clear idea they will be getting top notch service. I definitely want a drawing of myself on my mower. Phone # 555-271-0936
• design must work with parcelrelay.com/routeblanketmail guidelines

```html
<!DOCTYPE html>
<html lang="en">
<head>
<meta charset="utf-8">
<title>Dawson Lawn Cutting Service – Postcard</title>
<link rel="stylesheet" href="https://fonts.googleapis.com/css2?family=Arimo:ital,wght@0,400;0,700;1,700&family=PT+Serif:ital@0,400;1,400&family=Roboto:wght@300;400;500&display=swap">
<style>
:root{
  --stage:#e9e6e1;
  --sky:#29a6e0;
  --sky-deep:#1f93cf;
  --green:#2a9a46;
  --green-dark:#137a36;
  --green-light:#49b74c;
  --lime:#9bcb3c;
  --ink:#1d2430;
  --panel:rgba(70,70,72,.92);
  --white:#ffffff;
  --pink:#f6bfc9;
  --yellow:#fdf59c;
  --lawn:#5e8f3a;
  --lawn-sky:#c9d3da;
}
*{margin:0;padding:0;box-sizing:border-box}
html,body{width:1200px;height:534px;overflow:hidden;background:var(--stage)}
.card{position:absolute;width:566px;height:436px;background:var(--white);overflow:hidden;box-shadow:0 2px 8px rgba(0,0,0,.18)}
.card--front{left:24px;top:24px}
.card--back{left:610px;top:24px}
.abs{position:absolute}
.sans{font-family:"Roboto",Arial,sans-serif}
.serif{font-family:"PT Serif",Georgia,serif}
.bold-italic{font-family:"Arimo",Arial,sans-serif;font-weight:700;font-style:italic}

/* front */
.intro-banner{left:0;top:0;width:380px;height:108px}
.intro-text{left:18px;top:26px;color:var(--white);font-family:"Arimo",Arial,sans-serif;font-weight:700;font-size:15.5px;line-height:20px}
.intro-text span{display:block}
.intro-text span + span{padding-left:2px}
.mascot{background:linear-gradient(180deg,#9aa0a6 0%,#5a6a4a 55%,#d04a5a 100%);border-radius:6px}
.mascot--front{left:346px;top:28px;width:44px;height:76px}
.brand{font-family:"Roboto",Arial,sans-serif;font-weight:400;line-height:1}
.brand--front{left:396px;top:44px;color:var(--sky)}
.brand__name{display:block;font-size:42px;letter-spacing:.5px}
.brand__tag{display:block;font-size:14px;margin-top:2px;padding-left:2px}
.hello-band{left:0;top:116px;width:566px;height:36px;background:linear-gradient(90deg,var(--green-dark),var(--green) 45%,var(--green-light) 100%);color:var(--white);text-align:center;font-family:"PT Serif",Georgia,serif;font-style:italic;font-size:19px;line-height:36px}
.scene{left:0;top:156px;width:290px;height:196px;background:linear-gradient(180deg,var(--lawn-sky) 0%,#b9c2b6 38%,var(--lawn) 60%,#4f8130 100%)}
.services{left:290px;top:156px;width:276px;height:196px;background:var(--panel);color:var(--white)}
.services__title{left:24px;top:28px;font-family:"PT Serif",Georgia,serif;font-size:15px}
.services__rule{left:24px;top:48px;width:116px;height:2px;background:var(--lime)}
.services__list{left:14px;top:58px;width:258px;list-style:none;font-family:"Roboto",Arial,sans-serif;font-weight:300;font-size:12px;line-height:13.5px}
.services__list li{position:relative;padding-left:12px;margin-bottom:9px}
.services__list svg{position:absolute;left:0;top:2px}
.footer-green{left:0;top:352px;width:566px;height:84px;background:linear-gradient(90deg,var(--green-dark),var(--green) 50%,var(--green-light))}
.offer-strip{left:0;top:356px;width:460px;height:38px}
.offer-text{left:10px;top:366px;font-size:15.5px;color:var(--ink);letter-spacing:.1px}
.father-note{left:10px;top:403px;color:var(--white);font-family:"PT Serif",Georgia,serif;font-size:11px;line-height:14px}
.call{right:10px;top:378px;color:var(--white);font-family:"PT Serif",Georgia,serif;font-size:18px;text-align:right}
.phone{right:10px;top:402px;color:var(--white);font-family:"PT Serif",Georgia,serif;font-size:21px;display:flex;align-items:center;gap:3px}

/* back */
.back-head{left:0;top:0;width:434px;height:142px;background:linear-gradient(90deg,var(--green-dark),var(--green) 45%,var(--green-light))}
.value-line{left:32px;top:8px;color:var(--white);font-family:"Roboto",Arial,sans-serif;font-size:12.5px;display:flex;align-items:center;gap:6px}
.offer-small{left:24px;top:38px;color:var(--white);font-size:13.5px;line-height:16px;text-align:center;width:140px}
.offer-big{left:16px;top:72px;color:var(--white);font-size:30px;line-height:32px}
.mascot--back{left:244px;top:44px;width:40px;height:70px}
.brand--back{left:290px;top:50px;color:var(--white)}
.brand--back .brand__name{font-size:40px}
.brand--back .brand__tag{font-size:12.5px}
.phone--back{left:262px;top:112px;right:auto;font-family:"Arimo",Arial,sans-serif;font-weight:700;font-size:17px}
.zone{background:var(--pink);font-family:"Arimo",Arial,sans-serif;color:#111}
.zone--postage{left:434px;top:0;width:132px;height:142px;text-align:center;font-size:13px;line-height:17px;padding-top:62px}
.zone--yellow{left:0;top:142px;width:279px;height:294px;background:var(--yellow)}
.zone--address{left:279px;top:142px;width:287px;height:227px}
.zone--barcode{left:73px;top:369px;width:493px;height:67px;text-align:center;font-size:16px;line-height:67px}
.zone__title{position:absolute;left:0;top:36px;width:100%;text-align:center;font-size:16px}
.zone__note{position:absolute;font-size:11.5px;line-height:14px}
.zone--address .zone__note{left:30px;top:84px;width:240px}
.zone--yellow .zone__note{left:38px;top:84px;width:220px}
</style>
</head>
<body>

<section class="card card--front" aria-label="Postcard front">
  <svg class="abs intro-banner" viewBox="0 0 380 108" aria-hidden="true"><polygon points="0,0 380,0 268,108 0,108" fill="var(--sky)"/></svg>
  <p class="abs intro-text"><span>Marwick High School Junior Student</span><span>Earning Money For My College</span><span>Education</span></p>

  <div class="abs mascot mascot--front" role="img" aria-label="Cartoon of Dawson riding his mower"></div>
  <p class="abs brand brand--front"><span class="brand__name">Dawson</span><span class="brand__tag">Lawn Cutting Service</span></p>

  <h1 class="abs hello-band">Hi, All I Am Dawson</h1>

  <div class="abs scene" role="img" aria-label="Cartoon Dawson on his mower in front of a freshly cut lawn and farmhouse"></div>

  <div class="abs services">
    <h2 class="abs services__title">Service I Provide</h2>
    <div class="abs services__rule"></div>
    <ul class="abs services__list">
      <li><svg width="8" height="8" viewBox="0 0 8 8"><circle cx="4" cy="4" r="4" fill="#fff"/><path d="M2 4.2l1.4 1.4L6.2 2.6" stroke="var(--green)" stroke-width="1.3" fill="none"/></svg>Assunce of A Quality of Lawn Cutting Service</li>
      <li><svg width="8" height="8" viewBox="0 0 8 8"><circle cx="4" cy="4" r="4" fill="#fff"/><path d="M2 4.2l1.4 1.4L6.2 2.6" stroke="var(--green)" stroke-width="1.3" fill="none"/></svg>My Mower Weighs Half Of What Other Commercial Mowers Do</li>
      <li><svg width="8" height="8" viewBox="0 0 8 8"><circle cx="4" cy="4" r="4" fill="#fff"/><path d="M2 4.2l1.4 1.4L6.2 2.6" stroke="var(--green)" stroke-width="1.3" fill="none"/></svg>My Mower Does Not Throw Clippings Into Much Or Flower Beds</li>
      <li><svg width="8" height="8" viewBox="0 0 8 8"><circle cx="4" cy="4" r="4" fill="#fff"/><path d="M2 4.2l1.4 1.4L6.2 2.6" stroke="var(--green)" stroke-width="1.3" fill="none"/></svg>At An Additional Charge I Offer Bagging of The Clippings &amp;/ or Dog Waste Clean-up</li>
    </ul>
  </div>

  <div class="abs footer-green"></div>
  <svg class="abs offer-strip" viewBox="0 0 460 38" aria-hidden="true"><polygon points="0,0 460,0 424,38 0,38" fill="var(--sky)"/></svg>
  <p class="abs offer-text bold-italic">Book Me &nbsp;for 26 Week Season &amp; GET One Cut FREE</p>
  <p class="abs father-note">I am Working Side By Side With My Father, Who Operats His Own<br>Lawn Cutting Service For 20 Years</p>
  <p class="abs call">Call Us Today</p>
  <p class="abs phone"><svg width="18" height="18" viewBox="0 0 18 18" aria-hidden="true"><circle cx="9" cy="9" r="8" fill="none" stroke="#fff" stroke-width="1.3"/><path d="M6.4 4.6l1.6 2.2-1 1.1c.6 1.3 1.5 2.2 2.7 2.8l1.1-1 2.2 1.6-1 1.8c-3.3-.4-6.1-3.2-6.5-6.5z" fill="#fff"/></svg>555-271-0936</p>
</section>

<section class="card card--back" aria-label="Postcard back">
  <div class="abs back-head"></div>
  <p class="abs value-line"><svg width="12" height="12" viewBox="0 0 12 12" aria-hidden="true"><circle cx="6" cy="6" r="6" fill="#fff"/><path d="M3 6.2l2 2 4-4.4" stroke="#d0343a" stroke-width="1.6" fill="none"/></svg>Your property will continue to increase in value under &nbsp;our care.</p>
  <p class="abs offer-small bold-italic">Book Me for 26<br>Week Season &amp;</p>
  <p class="abs offer-big bold-italic">GET One<br>Cut FREE</p>

  <div class="abs mascot mascot--back" role="img" aria-label="Cartoon of Dawson riding his mower"></div>
  <p class="abs brand brand--back"><span class="brand__name">Dawson</span><span class="brand__tag">Lawn Cutting Service</span></p>
  <p class="abs phone phone--back"><svg width="20" height="20" viewBox="0 0 18 18" aria-hidden="true"><circle cx="9" cy="9" r="8" fill="none" stroke="#fff" stroke-width="1.3"/><path d="M6.4 4.6l1.6 2.2-1 1.1c.6 1.3 1.5 2.2 2.7 2.8l1.1-1 2.2 1.6-1 1.8c-3.3-.4-6.1-3.2-6.5-6.5z" fill="#fff"/></svg>555-271-0936</p>

  <div class="abs zone zone--postage">Postage<br>Area</div>
  <div class="abs zone zone--yellow">
    <p class="zone__note">This zone should contain no addresses that include a zip code or state. The delivery office will scan this entire area for recipient addresses and zip codes.</p>
  </div>
  <div class="abs zone zone--address">
    <h3 class="zone__title" style="font-weight:400">Address Area</h3>
    <p class="zone__note">The only text allowed in the Address Area is the recipient mailing address.<br>Red zones may have no text or graphics darker than 7% grayscale.</p>
  </div>
  <div class="abs zone zone--barcode">Barcode Area</div>
</section>

</body>
</html>
```